Need a Brochure Design

We need a brochure designed (A4 two sides or A3 foldable which is equal to 2 x A4 = total of four pages )

Brief and Logo attached.

```html
<!DOCTYPE html>
<html lang="en">
<head>
<meta charset="utf-8">
<title>Room &amp; Rest Staging – Booklet</title>
<link rel="stylesheet" href="https://fonts.googleapis.com/css2?family=Jost:wght@300;400;600&family=Playfair+Display:ital,wght@1,500&display=swap">
<style>
  :root{
    --backdrop:#c4c4c4;
    --page-cream:#efebe3;
    --page-blush:#ece3de;
    --peach:#f2e2d1;
    --ink:#3a3a3a;
    --ink-soft:#555;
    --coral:#e0a28f;
    --navy:#46506a;
    --gold:#d9c08f;
  }
  *{margin:0;padding:0;box-sizing:border-box}
  html,body{width:1200px;height:800px;overflow:hidden}
  body{background:var(--backdrop);font-family:'Jost',sans-serif;color:var(--ink);position:relative}
  .page{position:absolute;top:130px;width:382px;height:540px;overflow:hidden}
  .cover{left:15px;background:#e9e9e9}
  .page-left{left:415px;background:var(--page-cream)}
  .page-right{left:797px;background:var(--page-blush)}
  .photo{position:absolute}
  .abs{position:absolute}

  /* cover */
  .cover-photo{inset:0;background:linear-gradient(180deg,#e4e4e2 0%,#d9d8d6 45%,#cfcfcf 60%,#2b2b2b 85%,#1e1e1e 100%)}
  .cover-name{position:absolute;top:0;right:0;width:96px;height:96px;background:#fbf8f4;display:flex;align-items:center;justify-content:center;text-align:center;font-size:11px;font-weight:400;letter-spacing:.12em;text-transform:uppercase;color:var(--ink);line-height:1.4;padding:8px}

  /* left page */
  .hero-photo{left:20px;top:20px;width:342px;height:292px;background:linear-gradient(160deg,#f2f2f0 0%,#dcdad6 45%,#c9c6c0 70%,#e7e5e1 100%)}
  .caption{left:238px;top:298px;width:124px;height:60px;background:var(--peach);padding:9px 8px;text-align:right;font-size:5.5px;line-height:1.45;color:var(--ink-soft)}
  .caption strong{font-weight:600;color:var(--ink)}
  .headline{left:20px;top:356px;font-size:27px;font-weight:300;line-height:.98;letter-spacing:-.01em}
  .headline b{font-weight:600}
  .lede{left:20px;top:416px;width:230px;font-size:7.6px;text-transform:uppercase;letter-spacing:.02em;line-height:1.4}
  .body-col{top:448px;width:132px;font-size:6.6px;line-height:1.6}
  .col-a{left:82px}.col-b{left:228px}
  .body-col p+p{margin-top:8px}

  /* right page */
  .section-title{font-size:14px;font-weight:300;line-height:1.05}
  .section-title b{font-weight:600}
  .small{font-size:6.6px;line-height:1.65}
  .connected{left:18px;top:30px;width:132px;text-align:right}
  .connected .small{margin-top:8px}
  .photo-lounge{left:158px;top:24px;width:104px;height:168px;background:linear-gradient(170deg,#b9b4ab,#8a837b 55%,#d4cbbd)}
  .photo-kitchen{left:266px;top:28px;width:102px;height:168px;background:linear-gradient(170deg,#f1efeb,#cfc9c0 50%,#8d8a86)}
  .photo-bedroom{left:14px;top:212px;width:168px;height:104px;background:linear-gradient(160deg,#d7dbe2,#f4f2f0 50%,#d8c4c0)}
  .why{left:194px;top:220px;width:178px}
  .why ul{list-style:none;margin-top:8px}
  .why li{font-size:6.4px;line-height:1.75;padding-left:9px;position:relative}
  .why li::before{content:"";position:absolute;left:0;top:5px;width:2.5px;height:2.5px;border-radius:50%;background:var(--ink)}
  .referrals{left:16px;top:346px;width:170px}
  .referrals .small{margin-top:8px}
  .voucher-panel{left:10px;top:408px;width:170px;height:124px;background:var(--peach)}
  .voucher{position:absolute;left:18px;width:122px;height:50px;background:#fff;box-shadow:1px 1px 3px rgba(0,0,0,.12);display:flex;align-items:center;overflow:hidden}
  .voucher .wash{position:absolute;inset:0 30% 0 0;background:linear-gradient(90deg,#c9d0dc,#e9ecf1)}
  .voucher .label{position:relative;font-family:'Playfair Display',serif;font-style:italic;font-size:13px;color:var(--navy);padding-left:8px;line-height:1}
  .voucher .label small{display:block;font-family:'Jost',sans-serif;font-style:normal;font-size:3.6px;margin-top:3px;color:var(--ink-soft)}
  .voucher .tag{position:absolute;top:0;width:30px;height:44px;display:flex;align-items:center;justify-content:center;font-family:'Playfair Display',serif;font-style:italic;font-size:10px}
  .v1{top:10px}.v1 .tag{right:6px;background:var(--gold);color:var(--navy)}
  .v2{top:66px}.v2 .wash{inset:0 0 0 30%}.v2 .tag{left:4px;background:var(--navy);color:#fff}
  .v2 .label{padding-left:42px}
  .photo-team{left:200px;top:340px;width:166px;height:146px;background:linear-gradient(180deg,#e7e7e7 0%,#d9d9d9 40%,#8a8a8a 75%,#c49a4a 100%)}
  .contact{left:196px;top:490px;width:170px;border-top:1px solid var(--coral);border-bottom:1px solid var(--coral);padding:6px 0 5px;text-align:center;font-size:6.6px;line-height:1.5}
</style>
</head>
<body>

<section class="page cover">
  <div class="photo cover-photo" role="img" aria-label="Portrait of the lead stylist in a white blouse and layered grey necklace against a white brick wall"></div>
  <div class="cover-name">Room &amp; Rest Staging</div>
</section>

<section class="page page-left">
  <div class="photo hero-photo" role="img" aria-label="Bright staged open-plan living room and kitchen with white armchairs and pendant lights"></div>
  <div class="abs caption">
    <strong>House of Elm</strong><br>
    42 Harbour Lane, Southbank<br>
    Melbourne VIC 3006, Australia |<br>
    Market Price AUD 9M |<br>
    After Restaging AUD 10,35M
  </div>
  <h1 class="abs headline">Because <b>first</b><br><b>impressions</b> count</h1>
  <p class="abs lede">A gorgeous looking home sells faster and fetches a higher price.</p>
  <div class="abs body-col col-a">
    <p>At Room &amp; Rest Staging, we help our property clients create a lasting impression with minimal spend. Our property vendors are usually looking for home-staging on a tight budget. They come to us searching for creative transformations to help them</p>
  </div>
  <div class="abs body-col col-b">
    <p>sell well. Thoughtfully positioned furniture and on-trend interior décor can make all the difference!</p>
    <p>Our property styling service includes a free consultation, longer rental periods, and installation and removal.</p>
  </div>
</section>

<section class="page page-right">
  <div class="abs connected">
    <h2 class="section-title">We’re <b>well-<br>connected</b></h2>
    <p class="small">We have a steady flow of clients who have not yet secured their Real Estate Agents, so we’d be happy to share the love. We believe in last relationships, and we work with reputable agents across Melbourne.</p>
  </div>
  <div class="photo photo-lounge" role="img" aria-label="Staged lounge opening onto a courtyard"></div>
  <div class="photo photo-kitchen" role="img" aria-label="Styled sofa with teal cushions beside a kitchen"></div>
  <div class="photo photo-bedroom" role="img" aria-label="Two stylists dressing a bed with a pink knitted throw"></div>

  <div class="abs why">
    <h2 class="section-title">Why choose <b>Room &amp;<br>Rest Staging?</b></h2>
    <ul>
      <li>Experienced, enthusiastic property stylists</li>
      <li>Work with low client budgets</li>
      <li>Fast turnaround to a tight deadline</li>
      <li>Flexible rental terms (4/6/8 weeks)</li>
      <li>Happy to recommend potential customers</li>
    </ul>
  </div>

  <div class="abs referrals">
    <h2 class="section-title">We <b>Reward</b> Referrals!</h2>
    <p class="small">We offer a $200 gift voucher for every successful referral to us!</p>
  </div>
  <div class="abs voucher-panel">
    <div class="voucher v1">
      <div class="wash"></div>
      <div class="label">Gift Voucher<small>Valid for one styling service only</small></div>
      <div class="tag">$200</div>
    </div>
    <div class="voucher v2">
      <div class="wash"></div>
      <div class="tag">$200</div>
      <div class="label">Gift Voucher<small>Valid for one styling service only</small></div>
    </div>
  </div>

  <div class="photo photo-team" role="img" aria-label="The styling team of four women posed around a mustard armchair"></div>
  <div class="abs contact">
    We’d love to hear from you, so please<br>
    contact us by telephone, text, or email:<br>
    0400 000 123<br>
    hello@roomandreststaging.com.au
  </div>
</section>

</body>
</html>
```